We would like a simple company Christmas Card designed, based on our colours of orange and green and similar to a card that we printed last year (copy attached).

We would like a high res print ready PDF to provide to printer at the completion of the job.

Requirements
Must have
• Our Logo
• Colour scheme - orange (with some green for Christmas)
• Card size - A5 folded to finish size of A6
• Front cover text and image
• Front cover text: Celebrate your holidays with passion and fun
• Inside text and logo
• Inside text to read: Our warmest wishes for a wonderful Christmas and a very Happy New Year.

```html
<!DOCTYPE html>
<html lang="en">
<head>
<meta charset="utf-8">
<title>Holiday Card – Front and Inside</title>
<link rel="stylesheet" href="https://fonts.googleapis.com/css2?family=Questrial&family=Delius&family=Tinos:ital@1&display=swap">
<style>
  :root {
    --backdrop: #b3b3b3;
    --paper: #ffffff;
    --edge: #555555;
    --orange: #f08a33;
    --orange-soft: #f6b98a;
    --orange-faint: #f9d3b4;
    --green: #4aa64a;
    --green-soft: #9fd09f;
    --green-faint: #cfe8cf;
    --label: #111111;
  }
  * { box-sizing: border-box; margin: 0; padding: 0; }
  html, body { width: 1200px; height: 900px; overflow: hidden; }
  body {
    position: relative;
    background: var(--backdrop);
    font-family: "Questrial", "Helvetica Neue", Arial, sans-serif;
  }
  .card-front {
    position: absolute;
    left: 75px; top: 55px;
    width: 555px; height: 800px;
    background: var(--paper);
    border: 1.5px solid var(--edge);
  }
  .snowfall {
    position: absolute;
    left: 0; top: 0;
    width: 555px; height: 800px;
  }
  .front-message {
    position: absolute;
    left: 100px; top: 258px;
    width: 480px;
    text-align: center;
    color: var(--orange);
    font-size: 29px;
    line-height: 43px;
    letter-spacing: 0.3px;
  }
  .brand-name {
    position: absolute;
    left: 0; top: 728px;
    width: 555px;
    text-align: center;
    color: var(--orange);
    font-size: 34px;
    letter-spacing: 0.2px;
  }
  .card-inside {
    position: absolute;
    left: 691px; top: 399px;
    width: 467px; height: 383px;
    display: flex;
    background: var(--paper);
    border: 1.5px solid var(--edge);
  }
  .inside-panel { flex: 1; position: relative; }
  .inside-panel--left { border-right: 1.5px solid var(--edge); flex: 0 0 230px; }
  .inside-message {
    position: absolute;
    left: 0; top: 128px;
    width: 100%;
    text-align: center;
    font-family: "Delius", "Comic Sans MS", cursive;
    color: var(--orange);
    font-size: 14.5px;
    line-height: 18.5px;
  }
  .inside-label {
    position: absolute;
    left: 691px; top: 784px;
    width: 450px;
    text-align: center;
    font-family: "Tinos", "Times New Roman", serif;
    font-style: italic;
    font-size: 52px;
    color: var(--label);
  }
</style>
</head>
<body>
  <section class="card-front">
    <svg class="snowfall" viewBox="0 0 555 800" role="img" aria-label="Scattered orange and green snowflakes falling down the left side of the cover">
      <circle cx="73" cy="85" r="46" fill="var(--orange)" opacity="0.85"/>
      <circle cx="58" cy="217" r="37" fill="var(--green)" opacity="0.85"/>
      <circle cx="168" cy="190" r="25" fill="var(--orange)" opacity="0.8"/>
      <circle cx="96" cy="332" r="24" fill="var(--orange-soft)"/>
      <circle cx="157" cy="437" r="25" fill="var(--green-soft)"/>
      <circle cx="58" cy="494" r="17" fill="var(--orange-faint)"/>
      <circle cx="109" cy="598" r="10" fill="var(--green-faint)"/>
    </svg>
    <p class="front-message">Celebrate your holidays<br>with passion &amp; fun</p>
    <p class="brand-name">brightwater studio</p>
  </section>

  <section class="card-inside">
    <div class="inside-panel inside-panel--left"></div>
    <div class="inside-panel inside-panel--right">
      <p class="inside-message">Our warmest wishes<br>for a wonderful<br>Christmas<br>and<br>a very Happy New Year!</p>
    </div>
  </section>
  <p class="inside-label">Inside</p>
</body>
</html>
```